Copper Harbor Website Re-design

I want to update the design of my website with new branded logos (already created) as well as add more design/interactive elements.

This website acts a business overview website allowing customers to see what services we offer. We have recently added screen printing to our array of business services. I will want to add that to the site and also have a place for potential customers to fill out a form to receive a pricing quote.

www.copperharbor-example.net

Target Market(s)

Youth Sports Organizations, Schools, Businesses - Apparel

Industry/Entity Type

Retail/Service

Font styles to use
Sans Serif

Colors

Designer to choose only greyscale colors for use in the design.

```html
<!DOCTYPE html>
<html lang="en">
<head>
<meta charset="utf-8">
<title>Copper Harbor – Team Apparel and Uniforms</title>
<link rel="stylesheet" href="https://fonts.googleapis.com/css2?family=Orbitron:wght@500;600&family=Roboto:wght@400;500;700&display=swap">
<style>
:root{
  --black:#000;
  --ink:#111;
  --panel:#1c1c1c;
  --hero-a:#353535;
  --hero-b:#121212;
  --footer:#161616;
  --white:#fff;
  --text:#222;
  --muted:#6a6a6a;
  --line:#d6d6d6;
  --soft:#f3f3f3;
}
*{box-sizing:border-box;margin:0;padding:0}
html,body{width:1200px;height:3177px;overflow:hidden}
body{position:relative;background:var(--white);font-family:'Roboto',sans-serif;color:var(--text)}
.abs{position:absolute}
.display{font-family:'Orbitron',sans-serif;font-weight:500;letter-spacing:5px;text-transform:uppercase}

/* top bar */
.topbar{left:0;top:0;width:1200px;height:65px;background:var(--white)}
.contact-chip{display:flex;align-items:center;gap:12px;font-size:17px;font-weight:500;color:var(--ink)}
.chip-icon{width:36px;height:36px;border-radius:50%;background:var(--ink);display:flex;align-items:center;justify-content:center}
.navbar{left:0;top:65px;width:1200px;height:43px;background:var(--black)}
.nav{display:flex;gap:20px;font-size:14px;font-weight:500;color:var(--white)}
.brand-tab{left:522px;top:0;width:176px;height:108px}
.brand-name{left:522px;top:64px;width:176px;text-align:center;font-size:14px;font-weight:500;letter-spacing:2px;color:var(--ink);text-transform:uppercase}

/* hero */
.hero{left:0;top:108px;width:1200px;height:652px;background:linear-gradient(135deg,var(--hero-a),var(--hero-b) 70%)}
.hero-title{left:110px;top:148px;font-size:29px;line-height:37px;color:var(--white)}
.hero-sub{left:110px;top:280px;font-size:17px;font-weight:500;color:var(--white)}
.btn{display:inline-flex;align-items:center;gap:9px;font-weight:700;font-size:16px;text-transform:uppercase}
.btn-light{left:110px;top:325px;width:180px;height:52px;justify-content:center;background:var(--white);color:var(--ink)}
.btn-dark{background:var(--ink);color:var(--white);justify-content:center}
.hero-art{left:640px;top:40px;width:540px;height:470px;background:radial-gradient(ellipse at 55% 45%,#d8d8d8 0,#9a9a9a 40%,rgba(60,60,60,0) 72%)}

/* benefits */
.section-title{width:1200px;left:0;text-align:center;font-size:27px;color:var(--ink)}
.benefit{width:300px}
.benefit h3{font-size:16px;font-weight:700;color:var(--ink);margin-bottom:8px;text-transform:uppercase}
.benefit p{font-size:13px;line-height:21px;color:var(--muted)}
.benefit.left{text-align:right}
.b-icon{width:62px;height:62px;border-radius:50%;background:var(--ink);display:flex;align-items:center;justify-content:center}
.center-name{left:430px;top:1010px;width:340px;text-align:center;font-size:34px;font-weight:700;color:var(--ink);text-transform:uppercase;letter-spacing:3px}

/* services */
.services{left:0;top:1338px;width:1200px;height:840px}
.card{background:var(--white);border-radius:10px;padding:7px;text-align:center}
.card-photo{height:216px;border-radius:4px}
.card h3{font-size:16px;font-weight:700;color:var(--ink);margin:30px 0 12px;text-transform:uppercase}
.card p{font-size:14px;line-height:22px;color:var(--muted);padding:0 14px}
.card .btn{width:144px;height:42px;margin-top:23px;font-size:15px}

/* contact */
.contact-bg{left:0;top:2160px;width:1200px;height:560px;background:radial-gradient(ellipse at 50% 55%,#ececec 0,#f7f7f7 40%,var(--white) 75%)}
.field{border:1px solid var(--line);border-radius:26px;background:var(--white);font-size:14px;color:#8a8a8a;padding:0 26px;display:flex;align-items:center}
.field.area{border-radius:20px;align-items:flex-start;padding-top:22px}

/* footer */
.footer{left:0;top:2690px;width:1200px;height:430px;background:var(--footer)}
.f-head{font-size:18px;font-weight:700;color:var(--white);text-transform:uppercase}
.f-head::after{content:"";display:block;width:64px;height:2px;background:var(--white);margin-top:10px}
.f-links{list-style:none;font-size:12px;line-height:26px;color:var(--white)}
.f-row{display:flex;gap:18px;font-size:12px;color:var(--white);line-height:19px;margin-bottom:22px}
.f-text{font-size:12px;line-height:20px;color:var(--white)}
.subscribe{display:flex;width:252px;height:36px}
.subscribe .in{flex:1;background:var(--white);border-radius:18px 0 0 18px;font-size:10px;color:#777;display:flex;align-items:center;gap:6px;padding-left:14px}
.subscribe .go{width:48px;background:var(--black);border-radius:0 18px 18px 0;display:flex;align-items:center;justify-content:center}
.social{display:flex;gap:10px}
.social span{width:30px;height:30px;border-radius:50%;background:var(--white)}
.footer-name{font-size:30px;font-weight:700;color:var(--white);text-transform:uppercase;letter-spacing:2px;line-height:38px;text-align:center}
.bottombar{left:0;top:3120px;width:1200px;height:57px;background:var(--black);color:var(--white);font-size:13px}
.bottombar a{color:var(--white)}
</style>
</head>
<body>

<!-- header -->
<header class="abs topbar">
  <div class="abs contact-chip" style="left:110px;top:14px">
    <span class="chip-icon"><svg width="18" height="18" viewBox="0 0 24 24"><path fill="#fff" d="M6.6 10.8a15.1 15.1 0 0 0 6.6 6.6l2.2-2.2c.3-.3.7-.4 1-.2 1.1.4 2.3.6 3.6.6.6 0 1 .4 1 1V20c0 .6-.4 1-1 1A17 17 0 0 1 3 4c0-.6.4-1 1-1h3.5c.6 0 1 .4 1 1 0 1.3.2 2.5.6 3.6.1.3 0 .7-.2 1z"/></svg></span>
    555-201-4470
  </div>
  <div class="abs contact-chip" style="left:890px;top:14px;font-size:15px">
    <span class="chip-icon"><svg width="18" height="14" viewBox="0 0 24 18"><rect x="1" y="1" width="22" height="16" rx="2" fill="none" stroke="#fff" stroke-width="2"/><path d="M2 2l10 8 10-8" fill="none" stroke="#fff" stroke-width="2"/></svg></span>
    info@copperharbor-example.net
  </div>
</header>
<nav class="abs navbar">
  <div class="abs nav" style="left:110px;top:13px"><span>Team Uniform &amp; Spirit</span><span>Tournament Gear</span><span>Our Product</span></div>
  <div class="abs nav" style="left:756px;top:13px;gap:27px"><span>Enhancement Services</span><span>Our Clients</span><span>Contact Us</span></div>
</nav>
<svg class="abs brand-tab" viewBox="0 0 176 108"><polygon points="0,65 176,65 152,108 24,108" fill="#fff"/></svg>
<div class="abs brand-name" style="top:28px;font-size:15px;letter-spacing:3px;font-weight:700">Copper Harbor</div>

<!-- hero -->
<section class="abs hero">
  <div class="abs hero-art" role="img" aria-label="Photo of a yellow team jersey in front of a large white brand mark"></div>
  <h1 class="abs display hero-title">One-stop-shop for<br>all team apparel<br>and uniforms</h1>
  <p class="abs hero-sub">Creating Partnerships Through Uniforms And Apparel</p>
  <a class="abs btn btn-light">Learn More
    <svg width="15" height="15" viewBox="0 0 16 16"><circle cx="8" cy="8" r="8" fill="#111"/><path d="M6.5 4.5L10 8l-3.5 3.5" stroke="#fff" stroke-width="2" fill="none"/></svg></a>
  <svg class="abs" style="left:0;top:480px" width="1200" height="172" viewBox="0 0 1200 172">
    <polygon points="0,0 600,100 1200,0 1200,50 600,150 0,50" fill="#000"/>
    <polygon points="0,50 600,150 1200,50 1200,172 0,172" fill="#fff"/>
    <polygon points="600,98 632,130 600,162 568,130" fill="#000"/>
    <path d="M592 126l8 8 8-8" stroke="#fff" stroke-width="2.5" fill="none"/>
  </svg>
</section>

<!-- benefits -->
<h2 class="abs display section-title" style="top:828px">Our Benefits</h2>

<div class="abs benefit left" style="left:15px;top:895px"><h3>Organizations/Teams</h3><p>We provide organizations and<br>teams a partnership opportunity<br>through apparel.</p></div>
<div class="abs benefit left" style="left:15px;top:1013px"><h3>Free Online Store</h3><p>Each organization partner will be<br>provided with a free online store<br>with custom domain.</p></div>
<div class="abs benefit left" style="left:15px;top:1131px"><h3>No Minimum Order</h3><p>No minimum order for individual<br>spirit-wear orders for parents or<br>players.</p></div>

<div class="abs b-icon" style="left:339px;top:899px"><svg width="34" height="34" viewBox="0 0 34 34" fill="none" stroke="#fff" stroke-width="1.6"><circle cx="17" cy="11" r="4"/><path d="M10 23c0-4 3-6 7-6s7 2 7 6"/><circle cx="8" cy="15" r="3"/><circle cx="26" cy="15" r="3"/><path d="M3 25c0-3 2-5 5-5M31 25c0-3-2-5-5-5"/></svg></div>
<div class="abs b-icon" style="left:339px;top:1017px"><svg width="34" height="34" viewBox="0 0 34 34" fill="none" stroke="#fff" stroke-width="1.6"><rect x="9" y="4" width="14" height="26" rx="2"/><path d="M13 15h8l-1 6h-6z"/><path d="M15 15v-2a2 2 0 0 1 4 0v2"/></svg></div>
<div class="abs b-icon" style="left:339px;top:1135px"><svg width="34" height="34" viewBox="0 0 34 34" fill="none" stroke="#fff" stroke-width="1.6"><rect x="8" y="6" width="18" height="23" rx="2"/><path d="M13 6V4h8v2M12 13h10M12 18h10M12 23h6"/></svg></div>

<div class="abs center-name">Copper<br>Harbor</div>

<div class="abs b-icon" style="left:803px;top:899px"><svg width="34" height="34" viewBox="0 0 34 34" fill="none" stroke="#fff" stroke-width="1.6"><circle cx="17" cy="19" r="11"/><path d="M17 19v-6M17 19l4 3M14 4h6M17 4v4"/></svg></div>
<div class="abs b-icon" style="left:803px;top:1017px"><svg width="34" height="34" viewBox="0 0 34 34" fill="none" stroke="#fff" stroke-width="1.6"><path d="M6 29V21h5v8M14 29V16h5v13M22 29V11h5v18"/><path d="M5 15l8-6 5 3 10-8M24 4h4v4"/></svg></div>
<div class="abs b-icon" style="left:803px;top:1135px"><svg width="34" height="34" viewBox="0 0 34 34" fill="none" stroke="#fff" stroke-width="1.6"><circle cx="17" cy="17" r="13"/><circle cx="17" cy="17" r="10"/><text x="17" y="21.5" text-anchor="middle" fill="#fff" stroke="none" font-family="Roboto,sans-serif" font-size="11" font-weight="700">24</text></svg></div>

<div class="abs benefit" style="left:885px;top:895px"><h3>Fast Turnaround Time</h3><p>Quick turnaround with exceptional<br>customer service to provide the<br>best experience possible.</p></div>
<div class="abs benefit" style="left:885px;top:1013px"><h3>Revenue Generator</h3><p>Our partnership model allows for<br>organizations to earn commission<br>through our platforms.</p></div>
<div class="abs benefit" style="left:885px;top:1131px"><h3>24/7 Live Store</h3><p>24/7 Online Store allows<br>customers to purchase uniforms<br>and spirit-wear year round.</p></div>

<!-- enhancement services -->
<section class="abs services">
  <svg class="abs" style="left:0;top:0" width="1200" height="840" viewBox="0 0 1200 840">
    <polygon points="0,136 372,0 1200,136 1200,700 830,840 0,700" fill="#232323"/>
    <polygon points="0,150 372,24 1200,150 1200,690 830,815 0,690" fill="#161616"/>
  </svg>
  <h2 class="abs display section-title" style="top:135px;color:var(--white)">Enhancement Services</h2>
  <svg class="abs" style="left:42px;top:425px" width="26" height="42" viewBox="0 0 26 42"><path d="M22 3L5 21l17 18" stroke="#fff" stroke-width="4" fill="none"/></svg>
  <svg class="abs" style="left:1130px;top:425px" width="26" height="42" viewBox="0 0 26 42"><path d="M4 3l17 18L4 39" stroke="#fff" stroke-width="4" fill="none"/></svg>

  <article class="abs card" style="left:112px;top:210px;width:308px;height:443px">
    <div class="card-photo" role="img" aria-label="Photo of a multi-head embroidery machine stitching caps" style="background:linear-gradient(135deg,#d9d9d9,#8f8f8f 55%,#3c3c3c)"></div>
    <h3>Embroidery</h3>
    <p>Our 6-head state of the art embroidery machine allows us to customize product with flawless stitching.</p>
    <a class="btn btn-dark">Read More <svg width="14" height="14" viewBox="0 0 16 16"><circle cx="8" cy="8" r="8" fill="#fff"/><path d="M6.5 4.5L10 8l-3.5 3.5" stroke="#111" stroke-width="2" fill="none"/></svg></a>
  </article>
  <article class="abs card" style="left:446px;top:227px;width:308px;height:443px">
    <div class="card-photo" role="img" aria-label="Photo of a wide-format print and cut machine in a workshop" style="background:linear-gradient(180deg,#4a4a4a,#b5b5b5 55%,#5a4a40)"></div>
    <h3>Print/Cut System</h3>
    <p>Our 6-head state of the art embroidery machine allows us to customize product with flawless stitching.</p>
    <a class="btn btn-dark">Read More <svg width="14" height="14" viewBox="0 0 16 16"><circle cx="8" cy="8" r="8" fill="#fff"/><path d="M6.5 4.5L10 8l-3.5 3.5" stroke="#111" stroke-width="2" fill="none"/></svg></a>
  </article>
  <article class="abs card" style="left:780px;top:210px;width:308px;height:443px">
    <div class="card-photo" role="img" aria-label="Photo of a screen printing press with black shirts on the platens" style="background:linear-gradient(160deg,#cfcfcf,#8a9a7a 45%,#2a2a2a)"></div>
    <h3>Screen Printing</h3>
    <p>Our 6-head state of the art embroidery machine allows us to customize product with flawless stitching.</p>
    <a class="btn btn-dark">Read More <svg width="14" height="14" viewBox="0 0 16 16"><circle cx="8" cy="8" r="8" fill="#fff"/><path d="M6.5 4.5L10 8l-3.5 3.5" stroke="#111" stroke-width="2" fill="none"/></svg></a>
  </article>
</section>

<!-- contact -->
<div class="abs contact-bg" role="img" aria-label="Soft grey background texture"></div>
<h2 class="abs display section-title" style="top:2218px">Contact Us</h2>
<div class="abs field" style="left:194px;top:2292px;width:393px;height:52px">Name</div>
<div class="abs field" style="left:198px;top:2358px;width:393px;height:52px">Email Address</div>
<div class="abs field" style="left:198px;top:2424px;width:393px;height:52px">Phone Number</div>
<div class="abs field area" style="left:610px;top:2291px;width:396px;height:185px">Message</div>
<a class="abs btn btn-dark" style="left:500px;top:2517px;width:206px;height:52px">Pricing Quote <svg width="15" height="15" viewBox="0 0 16 16"><circle cx="8" cy="8" r="8" fill="#fff"/><path d="M6.5 4.5L10 8l-3.5 3.5" stroke="#111" stroke-width="2" fill="none"/></svg></a>

<!-- footer -->
<footer class="abs footer">
  <svg class="abs" style="left:0;top:-30px" width="1200" height="160" viewBox="0 0 1200 160">
    <polygon points="0,0 1200,0 1200,108 600,40 0,108" fill="#fff"/>
    <polygon points="0,108 600,40 1200,108 1200,148 600,80 0,148" fill="#000"/>
    <polygon points="600,8 632,40 600,72 568,40" fill="#000"/>
    <path d="M592 44l8-8 8 8" stroke="#fff" stroke-width="2.5" fill="none"/>
  </svg>
  <div class="abs footer-name" style="left:100px;top:200px;width:210px">Copper<br>Harbor</div>

  <div class="abs" style="left:377px;top:147px">
    <h4 class="f-head">Quick Links</h4>
    <ul class="f-links" style="margin-top:16px;padding-left:6px">
      <li>Team Uniform &amp; Spirit</li><li>Tournament Gear</li><li>Our Product</li><li>Enhancement Services</li><li>Our Clients</li><li>Contact Us</li>
    </ul>
  </div>

  <div class="abs" style="left:588px;top:147px">
    <h4 class="f-head">Contact Us</h4>
    <div style="margin-top:22px">
      <div class="f-row"><svg width="14" height="14" viewBox="0 0 24 24"><path fill="#fff" d="M6.6 10.8a15.1 15.1 0 0 0 6.6 6.6l2.2-2.2c.3-.3.7-.4 1-.2 1.1.4 2.3.6 3.6.6.6 0 1 .4 1 1V20c0 .6-.4 1-1 1A17 17 0 0 1 3 4c0-.6.4-1 1-1h3.5c.6 0 1 .4 1 1 0 1.3.2 2.5.6 3.6.1.3 0 .7-.2 1z"/></svg>555-201-4470</div>
      <div class="f-row"><svg width="14" height="12" viewBox="0 0 24 18"><rect x="0" y="0" width="24" height="18" rx="2" fill="#fff"/><path d="M1 1l11 8 11-8" fill="none" stroke="#161616" stroke-width="2"/></svg>info@copperharbor-example.net</div>
      <div class="f-row"><svg width="14" height="16" viewBox="0 0 24 28" style="margin-top:8px"><path fill="#fff" d="M12 0a9 9 0 0 0-9 9c0 7 9 19 9 19s9-12 9-19a9 9 0 0 0-9-9zm0 12a3 3 0 1 1 0-6 3 3 0 0 1 0 6z"/></svg><span>4200 W. Harbor Pkwy.<br>Lakeview, TX 75099</span></div>
      <div class="f-row"><svg width="14" height="14" viewBox="0 0 24 24"><rect x="2" y="8" width="20" height="13" rx="2" fill="#fff"/><rect x="6" y="2" width="12" height="7" fill="#fff"/><rect x="6" y="13" width="4" height="3" fill="#161616"/></svg>555-201-4471</div>
    </div>
  </div>

  <div class="abs" style="left:831px;top:147px">
    <h4 class="f-head">Subscribe To Our Blog</h4>
    <p class="f-text" style="margin:18px 0 16px 6px">Sign up today to get resources on how to<br>attract and retain more customers!</p>
    <div class="subscribe" style="margin-left:6px">
      <div class="in"><svg width="10" height="8" viewBox="0 0 24 18"><rect x="1" y="1" width="22" height="16" rx="2" fill="none" stroke="#777" stroke-width="2"/><path d="M2 2l10 8 10-8" fill="none" stroke="#777" stroke-width="2"/></svg>Email Address</div>
      <div class="go"><svg width="18" height="16" viewBox="0 0 24 22"><path fill="#fff" d="M23 1L1 10l7 3 2 8 4-6 6 4z"/></svg></div>
    </div>
    <div class="social" style="margin-top:20px" aria-label="Social media links"><span></span><span></span><span></span><span></span></div>
  </div>
</footer>

<div class="abs bottombar">
  <div class="abs" style="left:110px;top:20px">Copyright© 2021 <a style="text-decoration:underline;font-weight:500">copperharbor-example</a> &nbsp;| &nbsp;All Rights Reserved</div>
  <div class="abs" style="left:843px;top:20px">Terms and Conditions &nbsp;| &nbsp;&nbsp;Privacy Policy</div>
</div>

</body>
</html>
```